Modern, upmarket label design for food product

We need a label design for a food company producing nuts with sesame and honey. In fact, we would like the words "Cashews med sesam & honning" on the label (It's in Danish and means - Cashews with sesame & honey). It should be easy for the customer to quickly understand what it is.

It is a shelf product in the competitive food industry, which is why the design should wake the feeling of 'just wanting to grab the product down from the shelves'. So, the design should stand out and have an image of a cool, modern, hip product. This being said, I love a raw & handmade look.

The company is called Tyvo. Its origins are from the danish word Pilt that is a Danish slang for yummy. I have uploaded a photo of the package the products will be sold in.

Info & dimensions on bag in picture 1.
Dimensions: 6" x 9" | 15.2 cm x 22.3 cm
Capacity: 8 ounces | 250 grams (based on whole bean coffee)

Picture 2 is the same product, but has the possibility of attaching to a hanger on shelfs.

Picture 3 - I have also uploaded a photo of a product bag, where the hole is linear instead of a round hole. The designer chooses, which bag they will like to work with!

Please let me know if there are any questions!

Target Market(s)

Target market could really be any age, but the design needs to compel the target audience to pick it from the shelves. The package should signal a product you want to hold and have other people seeing you have it. The target audience is people who cares for what they buy, and typically doesn't want a low-end or budget product. They want the whole thing, meaning it has to taste good, look good etc. They are also the type of people who like to show off whatever products they buy by placing them in their houses for their guests to see. Or by uploading pictures of it on social medias.

Industry/Entity Type

It Company

Font styles to use
Other font styles liked:
• Not a must, but I like the 'Panton' script

Requirements
Must have
• My project must have the words 'Cashews med sesam & honning' on the label, so the customer will know within a second what they are looking at and buying.
Nice to have
• I am picturing the label with the words 'Cashews med sesam & honning' as a statement, again, emphasizing how the customer instantly should know what the product is. This being said, it should not be the only thing on the package and I love a raw & handmade look - which inspiration picture 5 is a great example of!
• I have uploaded photos of what I think looks good. With this said, I am not looking for a copy of those products, but see them as good inspiration. I have named the photos inspiration 1, 2, 3, 4 & 5.
• If needed, more text can be put on the label. For example 'vegan', 'laktosefri', Glutenfri', or 'Sund Snack' are great words for being used on the label.
Should not have
• The fonts on the label should not be too decorative. Personally I like an easy too read font.

```html
<!DOCTYPE html>
<html lang="da">
<head>
<meta charset="utf-8">
<title>Cashews med sesam &amp; honning – label</title>
<link rel="stylesheet" href="https://fonts.googleapis.com/css2?family=Alfa+Slab+One&family=Montserrat:wght@700;800&display=swap">
<style>
  :root {
    --paper-light: #f4eee4;
    --paper-mid: #e9dfcf;
    --paper-edge: #dccfb9;
    --ink-brown: #4a3426;
    --ink-brown-soft: #5b4232;
    --kraft: #c8a57a;
    --kraft-dark: #b8946a;
    --label-green: #a7c33c;
    --white: #ffffff;
  }
  html, body {
    margin: 0;
    padding: 0;
    width: 1200px;
    height: 2246px;
    overflow: hidden;
    background: var(--white);
  }
  .canvas {
    position: relative;
    width: 1200px;
    height: 2246px;
    overflow: hidden;
    background: var(--white);
  }

  /* Paper statement panel */
  .paper-panel {
    position: absolute;
    left: 0; top: 0;
    width: 1200px; height: 921px;
    background: radial-gradient(ellipse at 50% 45%, var(--paper-light) 0%, var(--paper-mid) 60%, var(--paper-edge) 100%);
  }
  .brand-name {
    position: absolute;
    display: flex;
    align-items: center;
    gap: 18px;
    font-family: "Montserrat", sans-serif;
    font-weight: 800;
    color: var(--ink-brown);
    letter-spacing: 2px;
  }
  .brand-name .brand-square {
    display: inline-block;
    background: var(--ink-brown);
  }
  .paper-panel .brand-name {
    left: 360px; top: 140px;
    font-size: 84px;
  }
  .paper-panel .brand-square { width: 54px; height: 54px; }

  .statement {
    position: absolute;
    left: 600px; top: 560px;
    transform: translate(-50%, -50%) rotate(-20deg);
    color: var(--ink-brown);
    text-align: left;
    white-space: nowrap;
    line-height: 1;
  }
  .statement .line-main {
    font-family: "Alfa Slab One", serif;
    font-size: 128px;
    letter-spacing: 2px;
    display: block;
    margin-left: -40px;
  }
  .statement .line-sub {
    font-family: "Montserrat", sans-serif;
    font-weight: 800;
    font-size: 118px;
    letter-spacing: 2px;
    display: block;
    margin-top: 6px;
  }
  .statement .line-sub.offset { margin-left: -20px; }

  /* Flat pouch */
  .pouch {
    position: absolute;
    left: 249px; top: 960px;
    width: 710px; height: 1230px;
    background: linear-gradient(180deg, var(--kraft) 0%, var(--kraft-dark) 100%);
    border-radius: 10px;
  }
  .label {
    position: absolute;
    left: 107px; top: 0;
    width: 496px; height: 800px;
    background: var(--label-green);
    border-radius: 0 0 248px 248px;
    text-align: center;
    color: var(--ink-brown);
  }
  .label .brand-name {
    left: 50%; top: 64px;
    transform: translateX(-50%);
    font-size: 46px;
  }
  .label .brand-square { width: 30px; height: 30px; }
  .label-title {
    position: absolute;
    left: 0; right: 0; top: 170px;
    line-height: 1.05;
  }
  .label-title .title-main {
    display: block;
    font-family: "Alfa Slab One", serif;
    font-size: 66px;
    letter-spacing: 1px;
  }
  .label-title .title-sub {
    display: block;
    font-family: "Montserrat", sans-serif;
    font-weight: 800;
    font-size: 52px;
    letter-spacing: 1px;
  }
  .badges {
    position: absolute;
    left: 0; right: 0; top: 420px;
    display: flex;
    justify-content: center;
    gap: 50px;
  }
  .badge {
    width: 98px; height: 98px;
    border: 4px solid var(--ink-brown);
    border-radius: 14px;
    box-sizing: border-box;
  }
  .label .brand-name.lower {
    top: 560px;
    font-size: 40px;
  }
  .label .brand-name.lower .brand-square { width: 26px; height: 26px; }
  .label-tagline {
    position: absolute;
    left: 0; right: 0; top: 660px;
    font-family: "Alfa Slab One", serif;
    font-size: 46px;
    letter-spacing: 2px;
    color: var(--ink-brown);
  }
  .net-weight {
    position: absolute;
    top: 1018px;
    font-family: "Montserrat", sans-serif;
    font-weight: 700;
    font-size: 26px;
    letter-spacing: 1px;
    color: var(--ink-brown);
  }
  .net-weight.imperial { left: 70px; }
  .net-weight.metric { right: 70px; }
</style>
</head>
<body>
<div class="canvas">

  <section class="paper-panel" role="img" aria-label="Crumpled raw paper texture in warm cream tones">
    <div class="brand-name"><span class="brand-square"></span>Tyvo</div>
    <h1 class="statement">
      <span class="line-main">CASHEWS</span>
      <span class="line-sub">MED SESAM</span>
      <span class="line-sub offset">&amp; HONNING</span>
    </h1>
  </section>

  <section class="pouch">
    <div class="label">
      <div class="brand-name"><span class="brand-square"></span>Tyvo</div>
      <h2 class="label-title">
        <span class="title-main">CASHEWS</span>
        <span class="title-sub">MED SESAM</span>
        <span class="title-sub">&amp; HONNING</span>
      </h2>
      <div class="badges">
        <div class="badge" aria-label="Gluten free badge"></div>
        <div class="badge" aria-label="Lactose free badge"></div>
        <div class="badge" aria-label="Suitable for vegans badge"></div>
      </div>
      <div class="brand-name lower"><span class="brand-square"></span>Tyvo</div>
      <div class="label-tagline">SUND SNACK</div>
    </div>
    <div class="net-weight imperial">8 OUNCES</div>
    <div class="net-weight metric">250 GRAMS</div>
  </section>

</div>
</body>
</html>
```